mortgage company professional business card

We would like to revamp our business card. Logos and current card attached.

Target Market(s)

white collar professionals

Industry/Entity Type

Mortgage Lender

Contact Information for Business Card

Looking for a sharp professional feel with white background for business card. No gloss. Looking for emboss.

Requirements
Must have
• -Professional touch
• -Emboss and raised lettering
• -Social media icons
• name, title, Phone, email, NMLS and web
• Complement logo and web

```html
<!DOCTYPE html>
<html lang="en">
<head>
<meta charset="utf-8">
<title>Homeward Lending – Business Card</title>
<link rel="stylesheet" href="https://fonts.googleapis.com/css2?family=Open+Sans:wght@400;600;700&display=swap">
<style>
  :root {
    --card-white: #fbfbfb;
    --navy: #262d6e;
    --green: #2e9e46;
    --text-gray: #7a7a7a;
    --social-1: #3b5a9a;
    --social-2: #d9473b;
    --social-3: #36a9e0;
    --social-4: #1f7bb6;
  }
  html, body {
    margin: 0;
    padding: 0;
    width: 1200px;
    height: 758px;
    overflow: hidden;
    background: var(--card-white);
  }
  .card {
    position: relative;
    width: 1200px;
    height: 758px;
    background: var(--card-white);
    font-family: "Open Sans", Arial, sans-serif;
    display: flex;
    flex-direction: column;
    align-items: center;
    box-sizing: border-box;
    padding-top: 185px;
  }
  .brand-block {
    display: flex;
    flex-direction: column;
    align-items: flex-end;
  }
  .brand {
    display: flex;
    align-items: center;
    gap: 16px;
  }
  .brand-mark {
    width: 54px;
    height: 54px;
    background: var(--green);
    border-radius: 50%;
  }
  .brand-name {
    font-size: 60px;
    font-weight: 700;
    color: var(--navy);
    letter-spacing: -0.5px;
    line-height: 1;
  }
  .tagline {
    margin-top: 10px;
    font-size: 24px;
    font-weight: 600;
    color: var(--text-gray);
    line-height: 1;
  }
  .person {
    margin-top: 40px;
    font-size: 32px;
    line-height: 1;
  }
  .person-name {
    font-weight: 700;
    color: var(--navy);
    letter-spacing: 0.5px;
  }
  .person-title {
    font-size: 24px;
    font-weight: 400;
    color: var(--green);
  }
  .contact {
    margin-top: 16px;
    font-size: 24px;
    color: var(--text-gray);
    text-align: center;
    line-height: 1.5;
  }
  .contact-label { margin-right: 4px; }
  .contact-item + .contact-item { margin-left: 18px; }
  .social {
    display: flex;
    gap: 6px;
    margin-top: 22px;
  }
  .social-dot {
    width: 40px;
    height: 40px;
    border-radius: 50%;
  }
  .social-dot--one { background: var(--social-1); }
  .social-dot--two { background: var(--social-2); }
  .social-dot--three { background: var(--social-3); }
  .social-dot--four { background: var(--social-4); }
</style>
</head>
<body>
  <main class="card">
    <div class="brand-block">
      <div class="brand">
        <span class="brand-mark"></span>
        <span class="brand-name">Homeward Lending</span>
      </div>
      <div class="tagline">Here for every step.</div>
    </div>

    <div class="person">
      <span class="person-name">EVAN MARLOW -</span>
      <span class="person-title">PRESIDENT</span>
    </div>

    <div class="contact">
      <div class="contact-address">2170 Harbor Lane, Elm Ridge, NY 11420</div>
      <div class="contact-lines">
        <span class="contact-item"><span class="contact-label">[p]</span>555 0142 7789</span>
        <span class="contact-item"><span class="contact-label">[e]</span>evan@homewardlend.com</span>
        <span class="contact-item"><span class="contact-label">[w]</span>www.homewardlend.com</span>
      </div>
    </div>

    <div class="social" aria-label="Social media links">
      <span class="social-dot social-dot--one"></span>
      <span class="social-dot social-dot--two"></span>
      <span class="social-dot social-dot--three"></span>
      <span class="social-dot social-dot--four"></span>
    </div>
  </main>
</body>
</html>
```